Business Card Design

Motorvane Ledger is an online automotive resource on a national scale specifically targeting lease purchases for new cars. Our Online and app platform allow prospective lease clients to scan a window sticker while at a franchise dealership and instantly receive a lease quote at what we call the sweet spot. Motorvane Ledger offers price transparency during the lease process to allow average people the confidence in the lease process and takes away any fear of the big franchise dealers.
Motorvane ledger allows ordinary lease customers to know they are getting a low price lease and not overpaying. Never overpay again

Industry/Entity Type

Automotive

Contact Information for Business Card

Motorvane Ledger
Martin Sowerby (President of operations)
Phone: 888-247-6031
Cell: 561-384-2706

```html
<!DOCTYPE html>
<html lang="en">
<head>
<meta charset="utf-8">
<title>Motorvane Ledger – Business Card</title>
<link rel="stylesheet" href="https://fonts.googleapis.com/css2?family=Montserrat:wght@400;500;700&display=swap">
<style>
  :root {
    --sky-top: #16181c;
    --sky-glow: #4a3f30;
    --horizon: #1a1a1a;
    --road: #2a2a2b;
    --ground: #0e0e0e;
    --accent: #fff200;
    --ink: #111111;
    --light: #ffffff;
  }
  * { margin: 0; padding: 0; box-sizing: border-box; }
  html, body { width: 1200px; height: 702px; overflow: hidden; background: #000; }
  .card {
    position: relative;
    width: 1200px;
    height: 702px;
    overflow: hidden;
    font-family: "Montserrat", sans-serif;
  }
  .card__scene {
    position: absolute;
    inset: 0;
    background:
      radial-gradient(ellipse 55% 18% at 50% 33%, rgba(120, 90, 55, 0.45), transparent 70%),
      radial-gradient(ellipse 18% 40% at 50% 80%, rgba(70, 70, 72, 0.55), transparent 75%),
      linear-gradient(180deg, var(--sky-top) 0%, #26262a 18%, var(--sky-glow) 30%, var(--horizon) 37%, var(--ground) 55%, #111 100%);
  }
  .contact {
    position: absolute;
    right: 74px;
    top: 268px;
    color: var(--light);
    text-align: right;
  }
  .contact__address {
    font-size: 29px;
    font-weight: 400;
    letter-spacing: 0.5px;
    margin-right: 8px;
  }
  .contact__row {
    display: flex;
    align-items: center;
    justify-content: flex-end;
    gap: 20px;
    font-size: 29px;
    font-weight: 400;
    letter-spacing: 0.5px;
  }
  .contact__row--office { margin-top: 42px; }
  .contact__row--mobile { margin-top: 20px; }
  .contact__icon { width: 36px; height: 40px; flex: none; }
  .band {
    position: absolute;
    left: 0;
    top: 488px;
    width: 1200px;
    height: 151px;
    background: var(--accent);
  }
  .brand {
    position: absolute;
    left: 58px;
    top: 28px;
    display: flex;
    align-items: center;
    gap: 16px;
    color: var(--ink);
  }
  .brand__mark { width: 26px; height: 26px; background: var(--ink); }
  .brand__name {
    font-size: 44px;
    font-weight: 700;
    line-height: 0.98;
    text-transform: uppercase;
    letter-spacing: -0.5px;
  }
  .person {
    position: absolute;
    right: 65px;
    top: 36px;
    text-align: right;
    color: var(--ink);
  }
  .person__name { font-size: 38px; font-weight: 500; line-height: 1.1; }
  .person__role { font-size: 28px; font-weight: 400; margin-top: 4px; }
</style>
</head>
<body>
  <div class="card">
    <div class="card__scene" role="img" aria-label="Blurred photograph of an empty road stretching to the horizon at dusk"></div>

    <div class="contact">
      <p class="contact__address">Business Address</p>
      <p class="contact__row contact__row--office">
        <span>888-247-6031</span>
        <svg class="contact__icon" viewBox="0 0 36 40" aria-hidden="true">
          <path d="M9 4 L15 4 L17 12 L12 16 Q15 25 22 30 L27 25 L34 28 L33 35 Q30 39 24 37 Q10 31 5 14 Q4 7 9 4 Z" fill="none" stroke="var(--accent)" stroke-width="3" stroke-linejoin="round"/>
        </svg>
      </p>
      <p class="contact__row contact__row--mobile">
        <span>561-384-2706</span>
        <svg class="contact__icon" viewBox="0 0 36 40" aria-hidden="true">
          <rect x="7" y="2" width="22" height="36" rx="3" fill="none" stroke="var(--accent)" stroke-width="3"/>
          <line x1="7" y1="31" x2="29" y2="31" stroke="var(--accent)" stroke-width="2"/>
          <circle cx="18" cy="34.5" r="1.4" fill="var(--accent)"/>
        </svg>
      </p>
    </div>

    <div class="band">
      <div class="brand">
        <span class="brand__mark" aria-hidden="true"></span>
        <p class="brand__name">Motorvane<br>Ledger</p>
      </div>
      <div class="person">
        <p class="person__name">Martin Sowerby</p>
        <p class="person__role">President of operations</p>
      </div>
    </div>
  </div>
</body>
</html>
```